Digital and Printed Promotional Flyer - Bramble Classic 2018

Fern Ridge Soccer Club needs a flyer created - both to be printed and also to distribute on social media and email (digital) that promotes the upcoming Bramble Classic (soccer) competition for October 2018. We need it to be colourful and stand out to promote the outstanding features:

* October 20-21 Competition 2018
* $5000 Minimum Winners Prize Pool
* Open Male
* Open Female
* Over 35 Male
* Over 35 Female
* Registrations Open September 1, 2018
* $500 team registration cost

Please see enclosed 2017 edition of the flyer. We will discuss with the winning candidate how to go about designing this, what to keep the same and what needs updating.

If you could provide some evidence of previous work or an idea for this project, that would be appreciated.

```html
<!DOCTYPE html>
<html lang="en">
<head>
<meta charset="utf-8">
<title>Bramble Classic 2018 – Fern Ridge Soccer Club</title>
<link href="https://fonts.googleapis.com/css2?family=Montserrat:wght@800;900&family=Roboto:ital,wght@0,400;0,500;0,700;1,400&family=Roboto+Condensed:wght@700&display=swap" rel="stylesheet">
<style>
  :root {
    --red: #e8202a;
    --splash: #ef4757;
    --ink: #3c3c3e;
    --grey: #4a4a4c;
    --paper: #ffffff;
    --muted: #555555;
  }
  * { margin: 0; padding: 0; box-sizing: border-box; }
  html, body { width: 872px; height: 1200px; overflow: hidden; background: var(--paper); }
  .flyer { position: relative; width: 872px; height: 1200px; background: var(--paper); font-family: "Roboto", sans-serif; color: var(--ink); }

  .club-mark { position: absolute; left: 336px; top: 120px; width: 200px; text-align: center; }
  .club-mark__dot { display: block; width: 64px; height: 64px; margin: 0 auto 14px; border-radius: 50%; background: var(--red); }
  .club-mark__name { font-family: "Roboto Condensed", sans-serif; font-weight: 700; font-size: 34px; color: var(--red); letter-spacing: 2px; }

  .player { position: absolute; top: 88px; width: 178px; height: 350px; background: linear-gradient(180deg, #4a4a4c, #3a3a3c); border-radius: 40px 40px 12px 12px; }
  .player--left { left: 70px; }
  .player--right { right: 64px; }
  .paint-burst { position: absolute; top: 320px; width: 96px; height: 96px; border-radius: 50%; background: radial-gradient(circle, #e8202a 0%, #ef4757 55%, rgba(239,71,87,0) 75%); }
  .paint-burst--left { left: 186px; }
  .paint-burst--right { right: 184px; }

  .club-name { position: absolute; left: 0; right: 0; top: 300px; text-align: center; font-family: "Roboto Condensed", sans-serif; font-weight: 700; font-size: 25px; line-height: 30px; color: var(--red); }
  .presents { position: absolute; left: 364px; top: 370px; width: 150px; height: 34px; background: var(--grey); color: #fff; font-size: 24px; line-height: 34px; text-align: center; letter-spacing: 1px; }

  .title { position: absolute; left: 0; right: 0; text-align: center; font-family: "Montserrat", sans-serif; font-weight: 900; letter-spacing: 4px; }
  .title--top { top: 426px; font-size: 48px; color: var(--ink); }
  .title--bottom { top: 486px; font-size: 50px; color: var(--red); }
  .dates { position: absolute; left: 0; right: 0; top: 556px; text-align: center; font-size: 29px; color: var(--ink); letter-spacing: 0.5px; }

  .crowd { position: absolute; left: 141px; top: 625px; width: 613px; height: 300px; background: linear-gradient(180deg, #ef4757 0%, #f05a68 100%); border-radius: 30px 60px 40px 70px; }
  .prize { position: absolute; left: 0; right: 0; top: 768px; text-align: center; color: #fff; font-style: italic; font-size: 29px; line-height: 38px; letter-spacing: 0.5px; }

  .features-tag { position: absolute; left: 362px; top: 937px; width: 146px; height: 36px; background: var(--red); color: #fff; font-weight: 700; font-size: 22px; line-height: 36px; text-align: center; }

  .details { position: absolute; left: 100px; top: 998px; width: 310px; text-align: right; font-size: 21px; line-height: 29px; }
  .details dt { font-weight: 700; color: var(--ink); }
  .details dd { font-weight: 500; color: var(--red); margin-bottom: 8px; }
  .divider { position: absolute; left: 443px; top: 1004px; width: 4px; height: 96px; background: var(--ink); }
  .categories { position: absolute; left: 483px; top: 998px; list-style: none; font-size: 23px; line-height: 30px; font-weight: 500; color: var(--ink); }

  .contact { position: absolute; left: 44px; right: 44px; top: 1144px; display: flex; justify-content: space-between; align-items: center; font-size: 16px; color: var(--muted); }
  .contact__item { display: flex; align-items: center; gap: 8px; }
  .contact__square { width: 15px; height: 15px; background: var(--red); border-radius: 2px; }
  .footer-band { position: absolute; left: 0; right: 0; bottom: 0; height: 28px; background: var(--red); }
</style>
</head>
<body>
<main class="flyer">
  <div class="club-mark">
    <span class="club-mark__dot"></span>
    <span class="club-mark__name">FRSC</span>
  </div>

  <div class="player player--left" role="img" aria-label="Silhouette of a running soccer player"></div>
  <div class="player player--right" role="img" aria-label="Silhouette of a running soccer player"></div>
  <div class="paint-burst paint-burst--left" role="img" aria-label="Red paint splash with a soccer ball"></div>
  <div class="paint-burst paint-burst--right" role="img" aria-label="Red paint splash with a soccer ball"></div>

  <h2 class="club-name">FERN RIDGE<br>SOCCER CLUB</h2>
  <div class="presents">Presents</div>

  <h1>
    <span class="title title--top">BRAMBLE</span>
    <span class="title title--bottom">CLASSIC 2018</span>
  </h1>
  <p class="dates">20 TO 21 OCTOBER 2018</p>

  <div class="crowd" role="img" aria-label="Red paint splash with cheering crowd silhouettes waving scarves"></div>
  <p class="prize">WINNER PRIZE POOL<br>$5000</p>

  <div class="features-tag">FEATURES:</div>

  <dl class="details">
    <dt>REGISTRATIONS OPEN</dt>
    <dd>SEPTEMBER 1, 2018</dd>
    <dt>TEAM REGISTRATION</dt>
    <dd>COST $500</dd>
  </dl>
  <div class="divider"></div>
  <ul class="categories">
    <li>Open Male</li>
    <li>Open Female</li>
    <li>Over 35 Male</li>
    <li>Over 35 Female</li>
  </ul>

  <div class="contact">
    <span class="contact__item">For more details please log on: <span class="contact__square"></span> /fernridgesoccerclub</span>
    <span class="contact__item">
      <svg width="20" height="15" viewBox="0 0 20 15" aria-hidden="true"><rect x="1" y="1" width="18" height="13" fill="none" stroke="#e8202a" stroke-width="1.6"/><polyline points="1,1 10,8.5 19,1" fill="none" stroke="#e8202a" stroke-width="1.6"/></svg>
      info@fernridgesoccerclub
    </span>
  </div>
  <div class="footer-band"></div>
</main>
</body>
</html>
```